Brake Test Training for Coal Mining

We offer Brake Test Training for Coal Mine workers. It's a legislative requirement that workers who are tasked with performing brake testing have certain competencies to do so. We test Light Vehicles and trailers, Heavy Vehicles and Mobile Mining Equipment like Graders, Scrapers and Dump Trucks.

```html
<!DOCTYPE html>
<html lang="en">
<head>
<meta charset="UTF-8">
<title>Ironbark Operator Training – Billboard</title>
<link href="https://fonts.googleapis.com/css2?family=Montserrat:wght@500;600;700;800;900&family=Oswald:wght@500&display=swap" rel="stylesheet">
<style>
  :root{
    --navy:#123d63;
    --navy-deep:#0d2f4f;
    --gold:#f5b800;
    --white:#ffffff;
    --ink:#141414;
    --page:#e9ecef;
  }
  *{box-sizing:border-box;margin:0;padding:0}
  html,body{width:1200px;height:1200px;overflow:hidden}
  body{background:var(--page);position:relative;font-family:"Montserrat",sans-serif}
  .billboard{position:absolute;left:40px;top:425px;width:1120px;height:350px;background:var(--white);overflow:hidden;box-shadow:0 6px 24px rgba(0,0,0,.15)}
  .photo{position:absolute;top:0;height:245px}
  .photo--haul-truck{left:0;width:330px;background:linear-gradient(90deg,rgba(255,255,255,0) 0%,rgba(255,255,255,0) 70%,#ffffff 100%),linear-gradient(180deg,#8796b8 0%,#a08a62 35%,#b8922e 60%,#7d7a72 100%)}
  .photo--loader{right:0;width:450px;background:linear-gradient(90deg,#ffffff 0%,rgba(255,255,255,0) 22%),linear-gradient(180deg,#c8b9a8 0%,#b89e6a 40%,#d6a92a 62%,#a8a396 100%)}
  .brand{position:absolute;left:300px;top:38px;width:420px;height:100px}
  .brand__rule{position:absolute;left:95px;right:0;height:4px}
  .brand__rule--top{top:0;background:var(--navy)}
  .brand__rule--bottom{top:88px;background:var(--gold)}
  .brand__dot{position:absolute;left:8px;top:10px;width:74px;height:74px;border-radius:50%;background:var(--navy)}
  .brand__name{position:absolute;left:110px;top:14px;font-weight:900;font-size:40px;letter-spacing:2px;color:var(--ink);line-height:1}
  .brand__sub{position:absolute;left:135px;top:60px;font-weight:500;font-size:19px;letter-spacing:1px;color:var(--ink);line-height:1}
  .contact{position:absolute;left:300px;top:152px;width:430px}
  .contact__phone{display:flex;align-items:center;gap:6px;font-weight:800;font-size:54px;color:var(--navy);line-height:1;letter-spacing:-1px}
  .contact__web{display:flex;align-items:center;gap:8px;margin:6px 0 0 20px;font-weight:700;font-size:24px;color:var(--ink);line-height:1}
  .band{position:absolute;left:0;right:0;top:245px;bottom:0;background:var(--navy-deep);border-top:5px solid var(--gold);display:flex;align-items:center}
  .band__lead{flex:0 0 258px;padding:0 8px 0 14px;text-align:right;color:var(--white);font-weight:600;font-size:12.5px;line-height:1.35;text-transform:uppercase;white-space:nowrap}
  .band__headline{margin-left:10px;font-family:"Oswald",sans-serif;font-weight:500;font-size:52px;color:var(--gold);letter-spacing:-1px;line-height:1;white-space:nowrap}
</style>
</head>
<body>
  <section class="billboard">
    <div class="photo photo--haul-truck" role="img" aria-label="Large yellow mining haul truck on a gravel site"></div>
    <div class="photo photo--loader" role="img" aria-label="Yellow wheel loader filling a dump truck at a rocky quarry face"></div>

    <div class="brand">
      <span class="brand__rule brand__rule--top"></span>
      <span class="brand__dot"></span>
      <span class="brand__name">IRONBARK</span>
      <span class="brand__sub">OPERATOR TRAINING</span>
      <span class="brand__rule brand__rule--bottom"></span>
    </div>

    <div class="contact">
      <div class="contact__phone">
        <svg width="34" height="42" viewBox="0 0 24 30" aria-hidden="true"><path d="M6 2l4 6-3 3c1.5 4 4 7.5 7 10l3-3 5 5-4 4C10 27 2 15 2 6z" fill="#141414"/><path d="M15 8a6 6 0 0 1 5 5M15 3a11 11 0 0 1 8 9" stroke="#141414" stroke-width="2" fill="none"/></svg>
        123.456.7890
      </div>
      <div class="contact__web">
        <svg width="22" height="22" viewBox="0 0 24 24" aria-hidden="true"><g fill="none" stroke="#123d63" stroke-width="1.8"><circle cx="12" cy="12" r="10"/><ellipse cx="12" cy="12" rx="4.5" ry="10"/><path d="M2 12h20M4 6.5h16M4 17.5h16"/></g></svg>
        www.yourwebsite.com
      </div>
    </div>

    <div class="band">
      <p class="band__lead">We test light vehicles and<br>trailers, heavy vehicles and<br>mobile mining equipment like</p>
      <h1 class="band__headline">GRADERS, SCRAPERS AND DUMP TRUCKS</h1>
    </div>
  </section>
</body>
</html>
```